Stationery Refresh For Local Mortgage Broker

We want to modernise and standardise our stationery, including: letterhead, presentation folder, email signature and business card.

The new stationery should be a more modern and professional take on our existing colour scheme and brand. (We do not want a complete overhaul.) A folder of approved stock photos can be found here: https://filebox.example-share.net/f/7kQzR2mTn4vWx9Lp3Yb8-HsdJe5Uc1Ga/view

Our current website is: www.brindlecovefin.com.au but we will be updating this to be consistent with our new stationery.

We are open to *very slight* tweaks to our logo if you feel it needs modernising, but overall we would like to maintain consistent colour scheme.

> Letterhead

148 Calloway Parade,
Geelong, VIC, 3220
ABN: 31 805 249 067
Australian Credit License: 718293

(03) 5391 6084
www.brindlecovefin.com.au

> Presentation Folder

148 Calloway Parade,
Geelong, VIC, 3220
(03) 5391 6084
www.brindlecovefin.com.au

ABN: 31 805 249 067

> Email Signature

Liam Tresidder
Director
M. 0412 857 294
P. (03) 5391 6084
www.brindlecovefin.com.au
148 Calloway Parade,
Geelong, VIC, 3220

ABN: 31 805 249 067

(you can also include a photo if you like: https://brindlecovefin.com.au/wp-content/uploads/2020/12/Liam-Tresidder.png.webp)

> Business Card

Liam Tresidder
Director
M. 0412 857 294
P. (03) 5391 6084
www.brindlecovefin.com.au
148 Calloway Parade,
Geelong, VIC, 3220

ABN: 31 805 249 067

Additional information...

If it's useful/relevant, the services we offer are: Home Loans, Investment Loans, Refinance, Debt Consolidation, Commercial Finance, Vehicle Loans
(You may choose to use this in any of the designs)

Target Market(s)

Home Buyers and Investors

Industry/Entity Type

Mortgage broking/property/real estate

Requirements
Must have
• At least somewhat consistent with our current site (yet meaningfully modernized)
Should not have
• dramatically different logo or colourscheme overhauls

```html
<!DOCTYPE html>
<html lang="en">
<head>
<meta charset="utf-8">
<title>Brindlecove Financial Services – Business Card</title>
<link rel="stylesheet" href="https://fonts.googleapis.com/css2?family=Montserrat:wght@400;500;700&family=Arimo:wght@400;700&display=swap">
<style>
  :root {
    --brand-red: #9b0a10;
    --brand-red-dark: #7d070c;
    --ink: #2a2a2a;
    --grey-band: #56575b;
    --paper: #ffffff;
    --backdrop: #e9e7e4;
    --tint: #f3d9da;
    --photo-top: #d9d5d2;
    --photo-bottom: #a9a4a2;
  }
  * { box-sizing: border-box; margin: 0; padding: 0; }
  html, body { width: 1200px; height: 900px; overflow: hidden; }
  body {
    background: var(--backdrop);
    display: flex; flex-direction: column; align-items: center; justify-content: center;
    gap: 46px;
    font-family: "Arimo", Arial, sans-serif;
  }
  .card {
    position: relative; width: 660px; height: 377px; overflow: hidden;
    box-shadow: 0 6px 18px rgba(0,0,0,.18);
  }

  /* Front */
  .card--front { background: var(--brand-red); color: var(--paper); }
  .card--front .brand-name {
    position: absolute; left: 0; right: 0; top: 128px; text-align: center;
    font-family: "Montserrat", sans-serif; font-weight: 400;
    font-size: 40px; letter-spacing: 13px; color: var(--paper);
  }
  .services {
    position: absolute; left: 0; right: 0; bottom: 52px; text-align: center;
    font-size: 17px; line-height: 1.45; color: var(--tint); letter-spacing: .3px;
  }
  .services .dot {
    display: inline-block; width: 8px; height: 8px; border-radius: 50%;
    background: var(--paper); margin: 0 6px; vertical-align: 2px;
  }

  /* Back */
  .card--back { background: var(--paper); }
  .portrait {
    position: absolute; right: 40px; top: 0; width: 230px; height: 290px;
    background: linear-gradient(180deg, var(--photo-top), var(--photo-bottom));
  }
  .swoosh { position: absolute; inset: 0; width: 100%; height: 100%; }
  .card--back .brand-name {
    position: absolute; left: 46px; top: 28px;
    font-family: "Montserrat", sans-serif; font-weight: 400;
    font-size: 30px; letter-spacing: 9px; color: var(--brand-red);
  }
  .contact { position: absolute; left: 52px; top: 84px; color: var(--ink); }
  .contact__name {
    font-family: "Montserrat", sans-serif; font-weight: 700;
    font-size: 26px; line-height: 1.2; color: var(--brand-red);
    text-transform: uppercase; letter-spacing: -.3px;
  }
  .contact__role { font-size: 17px; letter-spacing: .5px; margin-bottom: 8px; }
  .contact__address { font-size: 17px; line-height: 1.3; margin-bottom: 6px; }
  .contact__list { list-style: none; font-size: 17px; line-height: 1.3; }
  .contact__list li { display: flex; align-items: center; gap: 8px; }
  .contact__list svg { width: 15px; height: 15px; flex: none; }
  .legal {
    position: absolute; right: 26px; bottom: 30px; text-align: right;
    color: var(--paper); font-size: 16px; line-height: 1.4;
  }
</style>
</head>
<body>

  <section class="card card--front" aria-label="Business card front">
    <div class="brand-name">BRINDLECOVE</div>
    <p class="services">
      Home Loans<span class="dot"></span>Investment Loans<span class="dot"></span>Refinance<br>
      Debt Consolidation<span class="dot"></span>Commercial Finance<span class="dot"></span>Vehicle Loans
    </p>
  </section>

  <section class="card card--back" aria-label="Business card back">
    <div class="portrait" role="img" aria-label="Portrait photo of the director in a grey blazer"></div>
    <svg class="swoosh" viewBox="0 0 660 377" preserveAspectRatio="none" aria-hidden="true">
      <path d="M0 304 C220 316 430 286 570 188 C440 294 220 328 0 322 Z" fill="var(--grey-band)"/>
      <path d="M0 330 C250 336 490 282 660 150 L660 377 L0 377 Z" fill="var(--brand-red)"/>
    </svg>

    <div class="brand-name">BRINDLECOVE</div>

    <div class="contact">
      <h1 class="contact__name">Liam Tresidder</h1>
      <p class="contact__role">DIRECTOR</p>
      <p class="contact__address">148 Calloway Parade<br>Geelong, VIC, 3220</p>
      <ul class="contact__list">
        <li>
          <svg viewBox="0 0 24 24"><path d="M6.6 10.8a15 15 0 0 0 6.6 6.6l2.2-2.2c.3-.3.7-.4 1-.2 1.1.4 2.3.6 3.6.6.6 0 1 .4 1 1V20c0 .6-.4 1-1 1A17 17 0 0 1 3 4c0-.6.4-1 1-1h3.5c.6 0 1 .4 1 1 0 1.3.2 2.5.6 3.6.1.3 0 .7-.2 1z" fill="var(--brand-red)"/></svg>
          0412 857 294
        </li>
        <li>
          <svg viewBox="0 0 24 24"><rect x="6" y="2" width="12" height="20" rx="2" fill="none" stroke="var(--brand-red)" stroke-width="2"/><circle cx="12" cy="18.5" r="1.2" fill="var(--brand-red)"/></svg>
          (03) 5391 6084
        </li>
        <li>
          <svg viewBox="0 0 24 24" fill="none" stroke="var(--brand-red)" stroke-width="2"><circle cx="12" cy="12" r="9.5"/><path d="M2.5 12h19M12 2.5c3 3 3 16 0 19M12 2.5c-3 3-3 16 0 19"/></svg>
          www.brindlecovefin.com.au
        </li>
      </ul>
    </div>

    <p class="legal">ABN: 31 805 249 067<br>Australian Credit License: 718293</p>
  </section>

</body>
</html>
```